Letterhead and Business Card for Wealth Management Company
Harborline Wealth Management
Letterhead and Business Card for Wealth Management Company - Financial Services
Creative Brief
Use same font as used in my logo
Can use the same font or add additional font
Professional
R. Dwight Voss, CRPC®
Wealth Advisor
2450 Fernbrook Avenue Suite 310 Berwyn, PA 19312
dvoss@harborline-wealth.com
www.harborline-wealth.com
I work with affluent people so I want a sophisticated and classic looking business card and stationary. Our tagline is Dream. Plan. Live. with Live in italics. You can see it on our website at www.harborline-wealth.com. If appropriate, please include the tagline on the business card, letterhead and envelope. Please note the tagline on the website is a gradient color. It looks better printed in solid color.
Be creative.
dvoss dvoss
Thanks for all the great designs! I have a busy schedule today, but I will go through them and give star ratings later today or tonight. Thanks again!
Qwirk Qwirk

```html
<!DOCTYPE html>
<html lang="en">
<head>
<meta charset="utf-8">
<title>Harborline Wealth Management – Business Card</title>
<link rel="stylesheet" href="https://fonts.googleapis.com/css2?family=Cinzel:wght@600&family=Montserrat:wght@400;500;600&display=swap">
<style>
  :root {
    --navy: #1c3a6e;
    --navy-deep: #15305d;
    --gold: #c9a24a;
    --paper: #ffffff;
    --backdrop: #e9e6e1;
    --ink-soft: #3a4660;
  }
  * { margin: 0; padding: 0; box-sizing: border-box; }
  html, body { width: 1200px; height: 1086px; overflow: hidden; }
  body {
    background: var(--backdrop);
    display: flex; align-items: center; justify-content: center;
    font-family: "Montserrat", Arial, sans-serif;
  }
  .business-card {
    position: relative;
    width: 1000px; height: 570px;
    background: var(--paper);
    border-radius: 6px;
    box-shadow: 0 18px 40px rgba(0,0,0,.18);
    overflow: hidden;
  }
  .contact-panel { position: absolute; left: 0; top: 0; width: 520px; height: 570px; }
  .contact-group {
    position: absolute; right: 640px;
    color: var(--paper); text-align: right;
    font-size: 19px; line-height: 1.5; letter-spacing: .5px;
    white-space: nowrap;
  }
  .contact-group--phone { top: 100px; }
  .contact-group--address { top: 255px; }
  .contact-group--web { top: 410px; }
  .brand {
    position: absolute; left: 575px; top: 110px;
    display: flex; align-items: center; gap: 18px;
    color: var(--navy);
    font-family: "Cinzel", Georgia, serif; font-weight: 600;
  }
  .brand-square { width: 54px; height: 54px; background: var(--gold); flex: none; }
  .brand-name { line-height: 1.05; }
  .brand-name__main { display: block; font-size: 46px; letter-spacing: 2px; }
  .brand-name__sub { display: block; font-size: 15px; letter-spacing: 3.4px; margin-top: 6px; }
  .brand-rule {
    position: absolute; left: 647px; top: 215px;
    width: 290px; height: 3px; background: var(--gold);
  }
  .person { position: absolute; left: 647px; top: 270px; color: var(--navy); }
  .person-name { font-size: 30px; font-weight: 600; letter-spacing: 2px; text-transform: uppercase; }
  .person-title { font-size: 21px; font-weight: 400; color: var(--ink-soft); margin-top: 6px; letter-spacing: .8px; }
</style>
</head>
<body>
  <main class="business-card">
    <svg class="contact-panel" viewBox="0 0 520 570" aria-hidden="true">
      <path fill="var(--navy)" d="M0 0 H420 V80 A55 55 0 0 1 420 190 V230 A55 55 0 0 1 420 340 V385 A55 55 0 0 1 420 495 V570 H0 Z"/>
      <g fill="none" stroke="var(--paper)" stroke-width="2.5">
        <circle cx="440" cy="135" r="28"/>
        <circle cx="440" cy="285" r="28"/>
        <circle cx="440" cy="440" r="28"/>
      </g>
      <!-- phone -->
      <path fill="var(--paper)" d="M431 122 c3-2 6 0 7 3 l2 5 c1 2 0 4-2 5 l-2 1 c1 4 5 8 9 9 l1-2 c1-2 3-3 5-2 l5 2 c3 1 5 4 3 7 l-2 3 c-3 3-9 3-15-1 c-6-4-11-9-14-15 c-3-6-3-11 0-13 z"/>
      <!-- location pin -->
      <path fill="var(--paper)" d="M440 268 c-8 0-13 6-13 13 c0 9 13 22 13 22 s13-13 13-22 c0-7-5-13-13-13 z m0 8 a5 5 0 1 1 0 10 a5 5 0 1 1 0-10 z" fill-rule="evenodd"/>
      <!-- globe -->
      <g fill="none" stroke="var(--paper)" stroke-width="2">
        <circle cx="440" cy="440" r="14"/>
        <ellipse cx="440" cy="440" rx="6" ry="14"/>
        <line x1="426" y1="440" x2="454" y2="440"/>
        <line x1="429" y1="432" x2="451" y2="432"/>
        <line x1="429" y1="448" x2="451" y2="448"/>
      </g>
    </svg>

    <div class="contact-group contact-group--phone" style="right:640px">
      <p>012 555 0148</p>
      <p>012 555 0149</p>
    </div>
    <div class="contact-group contact-group--address">
      <p>2450 Fernbrook Avenue</p>
      <p>Suite 310, Berwyn, PA</p>
    </div>
    <div class="contact-group contact-group--web">
      <p>dvoss@harborline-wealth.com</p>
      <p>www.harborline-wealth.com</p>
    </div>

    <div class="brand">
      <span class="brand-square"></span>
      <span class="brand-name">
        <span class="brand-name__main">HARBORLINE</span>
        <span class="brand-name__sub">WEALTH MANAGEMENT</span>
      </span>
    </div>
    <div class="brand-rule"></div>

    <div class="person">
      <p class="person-name">R. Dwight Voss</p>
      <p class="person-title">Wealth Advisor</p>
    </div>
  </main>
</body>
</html>
```